Tempest Sealer - Postcard

tempestsealer.com

Tel ‪(941) 508-3174‬

Daniel Prewitt
daniel@tempestsealer.com

Design a postcard for a marketing campaign.

The problem is that all roofing vents leak. We have a product that goes into the vent that stops the roof from leaking.

In the last hurricane here in Florida, many houses were damaged because of water coming into the attic from the vents. The tempest sealer is a device that stops water from coming into the vents. This prevents water damage in the house. This stops mold from forming in the attic.

The tempest sealer offers this solution. It stops the rainwater from entering the roof through the roof vents. It stops water damages from occurring in the house which can cost 10s of thousands of dollars.

The target customer is a affluent, older couple 50-60 years old.

Target Market(s)

middle class to upper class adults / ages 50-60 years old (older but not VERY old)

Industry/Entity Type

roofing and construction

Font styles to use
Sans Serif

Colors
0054AA
0677BA
7BADD7
CADEEF
E8F1F8
0094D4
00A9DD
6FCCEA
C7EBF8
E9F6FB
FFF300
FFF600
FEFA6F
FFFEC7
FFFEE8
F0912C
F2A743
F7CA91
FBE8D2
FDF5EE

Requirements
Must have
• images of rain, wind, storm roofing, leaks, wet house, rain through interior ceilings, anxiety, storm damage
Nice to have
• feelings: professional / strong / reliable / safety / shelter / security / future stability

```html
<!DOCTYPE html>
<html lang="en">
<head>
<meta charset="utf-8">
<title>Tempest Sealer – Postcard</title>
<link href="https://fonts.googleapis.com/css2?family=Montserrat:wght@300;400;500;600;700;800;900&display=swap" rel="stylesheet">
<style>
  :root{
    --navy:#1d3470;
    --red:#a51d24;
    --brand-blue:#0054aa;
    --white:#ffffff;
    --ink:#111111;
    --page:#6b6869;
    --paper-top:#ffffff;
    --paper-bottom:#d6d6d6;
  }
  *{margin:0;padding:0;box-sizing:border-box}
  html,body{width:1200px;height:1200px;overflow:hidden}
  body{background:var(--page);font-family:"Montserrat",sans-serif;position:relative}
  .card{position:absolute;left:211px;width:778px;overflow:hidden;background:var(--white)}
  .card--front{top:45px;height:519px}
  .card--back{top:608px;height:518px}
  .card__shapes{position:absolute;inset:0;width:100%;height:100%}
  .abs{position:absolute}

  /* front */
  .brand{display:flex;align-items:center;gap:14px;left:22px;top:29px}
  .brand__dot{width:86px;height:86px;border-radius:50%;background:var(--brand-blue)}
  .brand__name{color:var(--brand-blue);font-weight:600;font-size:40px;line-height:40px;letter-spacing:.5px}
  .tagline{left:25px;top:142px;font-size:25px;line-height:27px;font-weight:500;color:var(--ink)}
  .tagline__rule{left:25px;top:199px;width:71px;height:3px;background:var(--navy)}
  .headline{left:23px;top:219px;font-weight:900;font-size:35px;line-height:34px;color:var(--navy);letter-spacing:-.5px}
  .headline__product{color:var(--red);display:block;margin-top:5px;line-height:31px}
  .offer{left:30px;top:386px;color:var(--white);font-weight:400;font-size:20px;line-height:21px;letter-spacing:-.3px}
  .offer__phone{left:29px;top:428px;color:var(--white);font-weight:800;font-size:40px;line-height:44px;letter-spacing:.5px}
  .contact-line{display:flex;align-items:center;gap:7px;color:var(--white);font-weight:500}
  .offer__email{left:30px;top:476px;font-size:17px}
  .inset{top:355px;width:191px;height:102px;border:3px solid var(--white)}
  .inset--roof{left:364px;background:linear-gradient(160deg,#8fa9c4 0%,#c9ad8e 25%,#b0916f 55%,#3c3630 100%)}
  .inset--ceiling{left:574px;background:linear-gradient(180deg,#d7d9dc 0%,#b9bcbf 55%,#c9c9c9 78%,#c8904e 88%,#b97c3c 100%)}
  .site{left:370px;top:471px;font-size:27px;font-weight:800;gap:10px}

  /* back */
  .back-brand{left:508px;top:42px;display:flex;align-items:center;gap:9px}
  .back-brand__dot{width:39px;height:39px;border-radius:50%;background:var(--ink)}
  .back-brand__name{color:var(--ink);font-weight:500;font-size:19px;line-height:19px}
  .product-shot{left:314px;top:45px;width:186px;height:186px;border-radius:50%;border:3px solid var(--white);
    background:radial-gradient(circle at 40% 35%,#cfd2d4 0%,#9a9da0 45%,#5e6164 80%,#8c8f91 100%)}
  .body-copy{left:16px;top:218px;width:322px;color:var(--white);font-size:11.2px;line-height:13px;text-align:justify;font-weight:400}
  .body-copy__cta{left:16px;top:354px;color:var(--white);font-weight:700;font-size:11.8px;line-height:17px}
  .rep__name{left:16px;top:400px;color:var(--white);font-weight:700;font-size:27px;line-height:30px}
  .rep__phone{left:16px;top:436px;font-size:26px;font-weight:700}
  .rep__email{left:19px;top:474px;font-size:16px}
  .rep__site{left:19px;top:496px;font-size:16px;font-weight:600}
  .icon{flex:none}
</style>
</head>
<body>

<section class="card card--front" aria-label="Postcard front">
  <svg class="card__shapes" viewBox="0 0 778 519" preserveAspectRatio="none">
    <defs>
      <linearGradient id="paper" x1="0" y1="0" x2="0" y2="1">
        <stop offset="0" stop-color="var(--paper-top)"/>
        <stop offset="1" stop-color="var(--paper-bottom)"/>
      </linearGradient>
      <linearGradient id="storm" x1="0" y1="0" x2="1" y2="1">
        <stop offset="0" stop-color="#9fb0b4"/>
        <stop offset=".35" stop-color="#3e5a52"/>
        <stop offset=".7" stop-color="#6f807e"/>
        <stop offset="1" stop-color="#a9b6b8"/>
      </linearGradient>
    </defs>
    <rect width="778" height="519" fill="url(#paper)"/>
    <polygon role="img" aria-label="Palm trees bending in hurricane wind and rain" points="510,0 778,0 778,428 277,428" fill="url(#storm)"/>
    <polygon points="479,0 510,0 386,227 354,227" fill="var(--red)"/>
    <polygon points="333,428 778,428 778,519 373,519" fill="var(--navy)"/>
    <polygon points="0,376 311,376 373,519 0,519" fill="var(--red)"/>
  </svg>

  <div class="abs brand">
    <span class="brand__dot"></span>
    <span class="brand__name">TEMPEST<br>SEALER</span>
  </div>

  <p class="abs tagline">Your Beautiful Florida<br>Home is Unprotected!</p>
  <span class="abs tagline__rule"></span>

  <h1 class="abs headline">PROTECT YOUR<br>HOME WITH THE<span class="headline__product">TEMPEST<br>SEALER</span></h1>

  <p class="abs offer">CALL TODAY FOR<br>SIMPLE PRICING!</p>
  <p class="abs offer__phone">941 508-3174</p>
  <p class="abs contact-line offer__email">
    <svg class="icon" width="15" height="13" viewBox="0 0 15 13"><rect x="1" y="3" width="13" height="9" fill="none" stroke="#fff" stroke-width="1.6"/><path d="M1 3l6.5 5L14 3" fill="none" stroke="#fff" stroke-width="1.6"/></svg>
    daniel@tempestsealer.com
  </p>

  <div class="abs inset inset--roof" role="img" aria-label="Tiled roof with a roof vent"></div>
  <div class="abs inset inset--ceiling" role="img" aria-label="Rainwater leaking through an interior ceiling"></div>

  <p class="abs contact-line site">
    <svg class="icon" width="20" height="20" viewBox="0 0 20 20"><circle cx="10" cy="10" r="8" fill="none" stroke="#fff" stroke-width="1.5"/><ellipse cx="10" cy="10" rx="3.5" ry="8" fill="none" stroke="#fff" stroke-width="1.3"/><path d="M2 10h16M3.5 6h13M3.5 14h13" stroke="#fff" stroke-width="1.2"/></svg>
    www.tempestsealer.com
  </p>
</section>

<section class="card card--back" aria-label="Postcard back">
  <svg class="card__shapes" viewBox="0 0 778 518" preserveAspectRatio="none">
    <defs>
      <linearGradient id="room" x1="0" y1="0" x2="1" y2="1">
        <stop offset="0" stop-color="#e6e4e1"/>
        <stop offset=".4" stop-color="#d9c6a8"/>
        <stop offset=".7" stop-color="#6b86a8"/>
        <stop offset="1" stop-color="#cfd2cf"/>
      </linearGradient>
    </defs>
    <rect role="img" aria-label="Smiling older couple relaxing at home" width="778" height="220" fill="url(#room)"/>
    <polygon points="0,208 423,208 341,399 0,399" fill="var(--navy)"/>
    <polygon points="513,0 778,0 778,518 398,518 336,399" fill="var(--white)"/>
    <polygon points="482,0 513,0 401,259 370,259" fill="var(--red)"/>
    <polygon points="0,399 329,399 398,518 0,518" fill="var(--red)"/>
  </svg>

  <div class="abs product-shot" role="img" aria-label="Installed roof vent sealer on a rooftop"></div>

  <div class="abs back-brand">
    <span class="back-brand__dot"></span>
    <span class="back-brand__name">TEMPEST<br>SEALER</span>
  </div>

  <p class="abs body-copy">Winds over 30 MPH push rainwater INTO your home through the rooftop vents! The result is water damage that can cost thousands of dollars to repair and remediate! The TEMPEST SEALER is a powerful roof vent protection system, engineered to block wind driven rains from entering your home's roof vents. The Tempest Sealer is made to withstand extreme conditions. Featuring IMPACT hurricane screening and powerful steel construction. Professional installation is permanent and concealed and is accomplished via the roof top.</p>
  <p class="abs body-copy__cta">GET PROTECTED FOR ALL THE STORMS AHEAD!<br>GET THE TEMPEST SEALER!</p>

  <p class="abs rep__name">DANIEL PREWITT</p>
  <p class="abs contact-line rep__phone">
    <svg class="icon" width="18" height="20" viewBox="0 0 18 20"><rect x="4" y="1" width="10" height="18" rx="2" fill="none" stroke="#fff" stroke-width="2"/><circle cx="9" cy="15.5" r="1.3" fill="#fff"/></svg>
    941 508-3174
  </p>
  <p class="abs contact-line rep__email">
    <svg class="icon" width="15" height="13" viewBox="0 0 15 13"><rect x="1" y="3" width="13" height="9" fill="none" stroke="#fff" stroke-width="1.6"/><path d="M1 3l6.5 5L14 3" fill="none" stroke="#fff" stroke-width="1.6"/></svg>
    daniel@tempestsealer.com
  </p>
  <p class="abs contact-line rep__site">
    <svg class="icon" width="15" height="15" viewBox="0 0 20 20"><circle cx="10" cy="10" r="8" fill="none" stroke="#fff" stroke-width="1.6"/><ellipse cx="10" cy="10" rx="3.5" ry="8" fill="none" stroke="#fff" stroke-width="1.4"/><path d="M2 10h16" stroke="#fff" stroke-width="1.4"/></svg>
    www.tempestsealer.com
  </p>
</section>

</body>
</html>
```